Custom Truck shop New Business Card design

double sided business card including my new logo, brand colors and picking a font I attached, clean and modern look. I attached the old card for some reference. and would like to include the picture of the white truck attached. I would also like to have it with one of my employees info as well. (same info except name and title Brin Tolvay Service Writer)

Dale Porvick
Owner

address
48310 E Calloway Ridge Rd S
STE 217
Marsh Hollow, CO 80219

phone 720-555-0184

email dale@brokenspurrigs.example

website brokenspurrgis.example

social @brokenspurrigs

Target Market(s)

men 18-60

Industry/Entity Type

Automotive

Contact Information for Business Card

Dale Porvick Owner address 48310 E Calloway Ridge Rd S STE 217 Marsh Hollow, CO 80219 phone 720-555-0184 email dale@brokenspurrigs.example website brokenspurrgis.example social @brokenspurrigs

Font styles to use
Other font styles liked:
• fonts attached

Requirements
Must have
• new logo, orange #FC68D, Charcoal #333333
Nice to have
• the white truck

```html
<!DOCTYPE html>
<html lang="en">
<head>
<meta charset="utf-8">
<title>Broken Spur Rigs – Business Card</title>
<link rel="stylesheet" href="https://fonts.googleapis.com/css2?family=Montserrat:wght@400;500;700&display=swap">
<style>
  :root {
    --orange: #e8794a;
    --charcoal: #333333;
    --charcoal-deep: #262626;
    --card-white: #f4f4f4;
    --text-grey: #4a4a4a;
    --backdrop: #d9d9d9;
  }
  * { box-sizing: border-box; margin: 0; padding: 0; }
  html, body { width: 1200px; height: 1200px; overflow: hidden; }
  body {
    background: var(--backdrop);
    font-family: "Montserrat", Arial, sans-serif;
    position: relative;
  }
  .card {
    position: absolute;
    left: 170px;
    width: 860px;
    height: 491px;
    border-radius: 26px;
    overflow: hidden;
    box-shadow: 0 6px 18px rgba(0,0,0,0.18);
  }
  .card--front { top: 80px; background: var(--charcoal); }
  .card--back { top: 629px; background: var(--card-white); }

  .front-texture {
    position: absolute; inset: 0;
    background: linear-gradient(120deg, #5a5a5a 0%, #404040 40%, var(--charcoal-deep) 100%);
  }
  .brand {
    position: absolute;
    display: flex;
    align-items: center;
    gap: 18px;
  }
  .brand__dot {
    border-radius: 50%;
    background: var(--orange);
    flex: none;
  }
  .brand__name {
    font-weight: 700;
    text-transform: uppercase;
    letter-spacing: 2px;
    white-space: nowrap;
  }
  .card--front .brand { right: 70px; top: 210px; }
  .card--front .brand__dot { width: 72px; height: 72px; }
  .card--front .brand__name { color: var(--orange); font-size: 30px; }

  .card--back .brand { right: 56px; top: 48px; gap: 14px; }
  .card--back .brand__dot { width: 48px; height: 48px; }
  .card--back .brand__name { color: var(--charcoal); font-size: 26px; }

  .person { position: absolute; left: 80px; top: 150px; }
  .person__name { color: var(--orange); font-weight: 700; font-size: 44px; letter-spacing: 0.5px; }
  .person__title { color: var(--text-grey); font-size: 21px; font-weight: 400; margin-top: 6px; margin-left: 14px; }

  .address {
    position: absolute; left: 80px; top: 268px;
    color: var(--text-grey); font-size: 20px; line-height: 28px; font-style: normal;
  }
  .contacts {
    position: absolute; left: 80px; top: 346px;
    list-style: none; color: var(--text-grey); font-size: 20px;
  }
  .contacts li { display: flex; align-items: center; gap: 12px; height: 30px; }
  .contacts svg { width: 20px; height: 20px; flex: none; }

  .social {
    position: absolute; right: 60px; top: 400px;
    display: flex; align-items: center; gap: 12px;
    color: var(--text-grey); font-size: 20px;
  }
  .social__mark { width: 18px; height: 18px; border: 2px solid var(--orange); border-radius: 50%; }
</style>
</head>
<body>

  <section class="card card--front">
    <div class="front-texture" role="img" aria-label="Charcoal background carrying a repeating pattern of the brand emblem"></div>
    <div class="brand">
      <span class="brand__dot"></span>
      <span class="brand__name">Broken Spur Rigs</span>
    </div>
  </section>

  <section class="card card--back">
    <div class="brand">
      <span class="brand__dot"></span>
      <span class="brand__name">Broken Spur Rigs</span>
    </div>

    <div class="person">
      <h1 class="person__name">Dale Porvick</h1>
      <p class="person__title">Owner</p>
    </div>

    <address class="address">
      48310 E Calloway Ridge Rd S STE<br>
      217 Marsh Hollow, CO 80219
    </address>

    <ul class="contacts">
      <li>
        <svg viewBox="0 0 24 24" aria-hidden="true"><path fill="#e8794a" d="M6.6 10.8c1.4 2.8 3.8 5.1 6.6 6.6l2.2-2.2c.3-.3.7-.4 1-.2 1.1.4 2.3.6 3.6.6.6 0 1 .4 1 1V20c0 .6-.4 1-1 1C10.6 21 3 13.4 3 4c0-.6.4-1 1-1h3.5c.6 0 1 .4 1 1 0 1.3.2 2.5.6 3.6.1.3 0 .7-.2 1z"/></svg>
        720-555-0184
      </li>
      <li>
        <svg viewBox="0 0 24 24" aria-hidden="true"><rect x="6" y="2" width="12" height="20" rx="2" fill="none" stroke="#e8794a" stroke-width="2.2"/><circle cx="12" cy="18" r="1.3" fill="#e8794a"/></svg>
        720-555-0147
      </li>
      <li>
        <svg viewBox="0 0 24 24" aria-hidden="true"><rect x="2" y="5" width="20" height="14" rx="1.5" fill="#e8794a"/><path d="M3 6l9 7 9-7" fill="none" stroke="#f4f4f4" stroke-width="1.8"/></svg>
        dale@brokenspurrigs.example
      </li>
      <li>
        <svg viewBox="0 0 24 24" aria-hidden="true"><circle cx="12" cy="12" r="9.5" fill="#e8794a"/><path d="M2.5 12h19M12 2.5c3 3 3 16 0 19M12 2.5c-3 3-3 16 0 19" fill="none" stroke="#f4f4f4" stroke-width="1.4"/></svg>
        www.brokenspurrgis.example
      </li>
    </ul>

    <div class="social">
      <span class="social__mark"></span>
      <span>@brokenspurrigs</span>
    </div>
  </section>

</body>
</html>
```